Church Lanterns Over Millbrook Gospel Booklet Design

We need a booklet designed that we will be printing to hand out in our community. Wording for each page will be provided and we need graphic design to produce the layouts in a format ready for print. Booklet will be 4.75" x 4.75" square and a total of 12 pages: 1 cover page front, 1 cover page back, 10 inside pages some of which will be full spread across 2 pages.

Target Market(s)

English speaking Westerners

Industry/Entity Type

Religious

Font styles to use
Serif

Colors
ffffff
85abd2
0292cd
33b8a4
5c5c5c

Requirements
Must have
• Minimalist design with clean look described in attached document
Nice to have
• Aesthetically pleasing graphics, crisp fonts, excellent turn around times
Should not have
• Effeminate design, busy look with too much graphic and text

```html
<!DOCTYPE html>
<html lang="en">
<head>
<meta charset="utf-8">
<title>Lanterns Over Millbrook – Gospel Booklet Layout</title>
<link rel="stylesheet" href="https://fonts.googleapis.com/css2?family=Lato:wght@400;700&family=Oswald:wght@500&display=swap">
<style>
  :root {
    --sheet: #e9eaeb;
    --dusk-1: #27398a;
    --dusk-2: #4a63b4;
    --dusk-3: #7390d2;
    --dusk-4: #4b64ae;
    --dusk-5: #2f4290;
    --dusk-6: #28357f;
    --band-a: #7a2d9f;
    --band-b: #b23190;
    --band-edge: #9d7ccf;
    --white: #ffffff;
    --title: #3a3a3a;
  }
  * { box-sizing: border-box; margin: 0; padding: 0; }
  html, body { width: 1200px; height: 3358px; overflow: hidden; }
  body { background: var(--sheet); font-family: "Lato", Arial, sans-serif; position: relative; }
  .defs { position: absolute; width: 0; height: 0; }

  .page {
    position: absolute; width: 509px; height: 506px; overflow: hidden;
    box-shadow: 3px 4px 8px rgba(0,0,0,.28);
  }
  .col-left { left: 87px; }
  .col-right { left: 607px; }
  .page-art { position: absolute; inset: 0; width: 100%; height: 100%; display: block; }

  .page-copy {
    position: absolute; left: 44px; right: 44px;
    color: var(--white); text-align: center; font-size: 16px; line-height: 1.5;
  }
  .page-copy.align-left { text-align: left; left: 56px; right: 56px; }
  .scripture { font-weight: 700; font-size: 32px; line-height: 1.38; margin-top: 30px; }
  .scripture.medium { font-size: 28px; line-height: 1.45; margin-top: 22px; }
  .scripture.small { font-size: 24px; line-height: 1.42; margin-top: 0; }
  .reference { font-size: 16px; font-weight: 700; margin-top: 22px; }
  .truths { margin: 26px 0 0 16px; font-size: 12.5px; line-height: 1.3; }
  .truths li { margin-bottom: 2px; }

  .folio {
    position: absolute; right: 34px; bottom: 0; width: 40px; height: 48px;
    border: 2px solid var(--white); border-bottom: none; border-radius: 14px 14px 0 0;
    color: var(--white); font-size: 25px; text-align: center; line-height: 48px;
  }

  .cover-title {
    position: absolute; top: 40px; right: 30px; width: 250px; padding: 16px 0 0 18px;
    font-family: "Oswald", "Arial Narrow", sans-serif; font-weight: 500;
    font-size: 46px; line-height: 1.02; color: var(--title); text-transform: uppercase;
  }
  .cover-title::before, .cover-title::after { content: ""; position: absolute; background: var(--title); }
  .cover-title::before { top: 0; left: 0; width: 250px; height: 3px; }
  .cover-title::after { top: 0; right: 0; width: 3px; height: 160px; }
</style>
</head>
<body>

<svg class="defs" aria-hidden="true">
  <defs>
    <linearGradient id="dusk" x1="0" y1="0" x2="0" y2="1">
      <stop offset="0" stop-color="var(--dusk-1)"/>
      <stop offset=".35" stop-color="var(--dusk-2)"/>
      <stop offset=".52" stop-color="var(--dusk-3)"/>
      <stop offset=".64" stop-color="var(--dusk-4)"/>
      <stop offset=".8" stop-color="var(--dusk-5)"/>
      <stop offset="1" stop-color="var(--dusk-6)"/>
    </linearGradient>
    <linearGradient id="band" x1="0" y1="0" x2="1" y2="0">
      <stop offset="0" stop-color="var(--band-a)"/>
      <stop offset="1" stop-color="var(--band-b)"/>
    </linearGradient>
    <radialGradient id="glow" cx=".42" cy=".5" r=".75">
      <stop offset="0" stop-color="#fffbe8"/>
      <stop offset=".35" stop-color="#f7d889"/>
      <stop offset=".75" stop-color="#d98a3c"/>
      <stop offset="1" stop-color="#a8632e"/>
    </radialGradient>
    <radialGradient id="violet-light" cx=".5" cy=".3" r=".75">
      <stop offset="0" stop-color="#ffffff"/>
      <stop offset=".3" stop-color="#cdb5e6"/>
      <stop offset=".7" stop-color="#8a62b4"/>
      <stop offset="1" stop-color="#5a3b86"/>
    </radialGradient>
    <symbol id="dusk-scene" viewBox="0 0 500 500" preserveAspectRatio="none">
      <rect width="500" height="500" fill="url(#dusk)" role="img" aria-label="Illustration of layered blue mountain ridges at dusk"/>
    </symbol>
    <symbol id="band-right" viewBox="0 0 500 500" preserveAspectRatio="none">
      <path d="M0 336 C150 350 340 400 500 446" fill="none" stroke="var(--band-edge)" stroke-width="3"/>
      <path d="M0 344 C150 358 340 408 500 454 V500 H0Z" fill="url(#band)"/>
    </symbol>
  </defs>
</svg>

<!-- Row 1 -->
<section class="page col-left" style="top:98px">
  <svg class="page-art" viewBox="0 0 500 500" preserveAspectRatio="none"><use href="#dusk-scene"/></svg>
</section>
<section class="page col-right" style="top:98px">
  <svg class="page-art" viewBox="0 0 500 500" preserveAspectRatio="none">
    <rect width="500" height="500" fill="url(#glow)" role="img" aria-label="Photo of hands pressed together in prayer against a bright sunlit sky"/>
    <path d="M0 420 C150 400 330 420 500 400 V500 H0Z" fill="url(#band)"/>
  </svg>
  <h1 class="cover-title">Lanterns Over Millbrook</h1>
</section>

<!-- Row 2 -->
<section class="page col-left" style="top:629px">
  <svg class="page-art" viewBox="0 0 500 500" preserveAspectRatio="none">
    <rect width="500" height="500" fill="url(#violet-light)" role="img" aria-label="Photo of an open hand reaching toward a glowing cross in violet clouds"/>
    <use href="#band-right" transform="translate(500 0) scale(-1 1)"/>
  </svg>
  <span class="folio">2</span>
</section>
<section class="page col-right" style="top:629px">
  <svg class="page-art" viewBox="0 0 500 500" preserveAspectRatio="none"><use href="#dusk-scene"/><use href="#band-right"/></svg>
  <div class="page-copy" style="top:62px">
    <p>God willingly created the universe,<br>meaning he envisioned, designed, and made us.</p>
    <p class="scripture">“In the beginning God<br>created the heavens and<br>the earth.”</p>
    <p class="reference">(Genesis 1:1)</p>
  </div>
  <span class="folio">3</span>
</section>

<!-- Row 3 -->
<section class="page col-left" style="top:1162px">
  <svg class="page-art" viewBox="0 0 500 500" preserveAspectRatio="none"><use href="#dusk-scene"/><use href="#band-right" transform="translate(500 0) scale(-1 1)"/></svg>
  <div class="page-copy align-left" style="top:42px">
    <p>This reality establishes some<br>foundational truths for all of us:</p>
    <ol class="truths">
      <li>God loves us - he didn't have to create us; we are here because he couldn't imagine life without us.</li>
      <li>God is the proper authority in our lives - if he designed and made us, he rightfully owns us.</li>
      <li>God knows the purpose of our lives - if he designed and made us, he knows why we are here.</li>
      <li>God's truth is the truth we need - if he designed and made us, he knows what it takes for life to go well for us.</li>
    </ol>
  </div>
  <span class="folio">4</span>
</section>
<section class="page col-right" style="top:1162px">
  <svg class="page-art" viewBox="0 0 500 500" preserveAspectRatio="none"><use href="#dusk-scene"/><use href="#band-right"/></svg>
  <div class="page-copy" style="top:34px;font-size:15px;line-height:1.45">
    <p>God willingly created the universe, meaning he envisioned, designed, But we, mankind, have all rejected God's authority in our lives. And because he rightfully owns us, our rebellion against God is a grave injustice; an act of treason for which we deserve to be cut off from God forever. and made us.</p>
    <p class="scripture" style="margin-top:18px">“For the wages of sin<br>is death...”</p>
    <p class="reference" style="margin-top:16px">(Romans 6:23)</p>
  </div>
  <span class="folio">5</span>
</section>

<!-- Row 4 -->
<section class="page col-left" style="top:1693px">
  <svg class="page-art" viewBox="0 0 500 500" preserveAspectRatio="none"><use href="#dusk-scene"/><use href="#band-right" transform="translate(500 0) scale(-1 1)"/></svg>
  <div class="page-copy" style="top:40px">
    <p>This alienation from God is evident in a myriad of ways including poverty, crime, conflict in our relationships, and our internal struggles. But worse, when we die, we must face the consequences for our rejection of God by spending eternity in hell - a lake of fire created by God as the place where our treason is brought to justice.</p>
  </div>
  <span class="folio">6</span>
</section>
<section class="page col-right" style="top:1693px">
  <svg class="page-art" viewBox="0 0 500 500" preserveAspectRatio="none"><use href="#dusk-scene"/><use href="#band-right"/></svg>
  <div class="page-copy" style="top:40px">
    <p>But God does not want you to pay for your own sins. God loves us so much he sent his only son to save us. Jesus Christ died on the cross to serve our sentence for our rebellion against God and rose again on the third day. Since Christ paid our full penalty, we can be completely forgiven and reconciled to God.</p>
    <p class="scripture medium">“For God so loved the world that he sent his one and only son that whosoever believes in him will not perish but have eternal life.”</p>
    <p class="reference">(John 3:16)</p>
  </div>
  <span class="folio">7</span>
</section>

<!-- Row 5 -->
<section class="page col-left" style="top:2223px">
  <svg class="page-art" viewBox="0 0 500 500" preserveAspectRatio="none"><use href="#dusk-scene"/><use href="#band-right" transform="translate(500 0) scale(-1 1)"/></svg>
  <div class="page-copy" style="top:18px">
    <p>First, ask Jesus Christ to save you (Since he is God, he can hear you): Acknowledge that God is the rightful authority of the universe and your life. Apologize to him for your rebellion against God. Ask Jesus Christ to come into your life as your Lord and Savior. This decision will immediately trigger his miracle of salvation in you. God now lives in you!</p>
  </div>
  <span class="folio">8</span>
</section>
<section class="page col-right" style="top:2223px">
  <svg class="page-art" viewBox="0 0 500 500" preserveAspectRatio="none"><use href="#dusk-scene"/><use href="#band-right"/></svg>
  <div class="page-copy" style="top:42px">
    <p class="scripture small">“If you confess with your mouth that Jesus is Lord and believe in your heart that God raised him from the dead, you will be saved.”</p>
    <p class="reference" style="margin-top:6px">(Romans 10:9)</p>
  </div>
  <span class="folio">9</span>
</section>

<!-- Row 6 -->
<section class="page col-left" style="top:2756px">
  <svg class="page-art" viewBox="0 0 500 500" preserveAspectRatio="none"><use href="#dusk-scene"/><use href="#band-right" transform="translate(500 0) scale(-1 1)"/></svg>
  <div class="page-copy" style="top:36px">
    <p>Next, God has given us the Bible and his church as the key tools for us to grow in our understanding of God and our personal relationship with him. So, it is essential you find a local church that believes the Bible is 100% true. Tell one of the pastors you are a brand new Christian and they will help you from there.</p>
  </div>
  <span class="folio">10</span>
</section>
<section class="page col-right" style="top:2756px">
  <svg class="page-art" viewBox="0 0 500 500" preserveAspectRatio="none"><use href="#dusk-scene"/><use href="#band-right"/></svg>
  <span class="folio">11</span>
</section>

</body>
</html>
```